Redesign of Real Estate Agency Website

We need a redesign for our real estate agency website. Please see attached creative brief.

Target Market(s)

Refer to creative brief.

Industry/Entity Type

Real Estate

Requirements
Must have
• Refer to creative brief.

```html
<!DOCTYPE html>
<html lang="en">
<head>
<meta charset="utf-8">
<title>Palmcove Realty – Phuket Property and Real Estate for Sale</title>
<link href="https://fonts.googleapis.com/css2?family=Questrial&display=swap" rel="stylesheet">
<style>
:root{
  --ink:#2b2b2b;
  --blue:#1f8fd6;
  --brand-blue:#1a5fa8;
  --red:#d9262b;
  --panel-top:#fbfbfb;
  --panel-bottom:#e9e9e9;
  --select-bg:#eeeeee;
  --select-arrow:#5ec7ee;
  --map-box:#d8d8d8;
  --map-fill:#d3ddd4;
  --bg:#ffffff;
  --bg-edge:#e6e6e6;
}
*{margin:0;padding:0;box-sizing:border-box}
html,body{width:1200px;height:980px;overflow:hidden}
body{
  background:radial-gradient(ellipse at 50% 55%,var(--bg) 60%,var(--bg-edge) 100%);
  font-family:"Questrial",sans-serif;color:var(--ink);
}
.page{position:absolute;left:0;top:0;width:980px;height:800px;transform:scale(1.2245);transform-origin:0 0}
.page *{position:absolute}
.brand{left:197px;top:88px;font-size:20px;line-height:22px;color:var(--brand-blue);letter-spacing:-.3px;white-space:nowrap}
.tagline{left:350px;top:103px;font-size:6px;line-height:8px;white-space:nowrap}
.nav a{top:137px;font-size:10px;color:var(--ink);text-decoration:none;white-space:nowrap}
.nav a.current{color:var(--blue)}
.hero{left:187px;top:162px;width:616px;height:190px;border-radius:7px;
  background:linear-gradient(var(--panel-top),var(--panel-bottom));
  box-shadow:0 2px 5px rgba(0,0,0,.3)}
.select{left:37px;width:93px;height:10px;background:linear-gradient(#fafafa,var(--select-bg));
  border:1px solid #cfcfcf;font-size:5.5px;line-height:8px;padding-left:5px;white-space:nowrap}
.select::after{content:"";position:absolute;right:0;top:0;width:9px;height:8px;background:var(--select-arrow)}
.search-btn{left:46px;top:163px;width:72px;height:16px;border-radius:8px;
  background:linear-gradient(#aee6f8,#58c1ea);color:#1b5e87;font-size:10px;text-align:center;line-height:16px}
.feature-title{font-size:12px;color:var(--blue);white-space:nowrap}
.photo{box-shadow:3px 3px 5px rgba(0,0,0,.45)}
.photo.condo{background:linear-gradient(180deg,#c9dde6 0%,#e8eef0 45%,#3aa3c9 80%,#2d7fa8 100%)}
.photo.villa{background:linear-gradient(180deg,#6c5e56 0%,#3b2d27 45%,#a6794c 70%,#8d8a86 100%)}
.section-title{font-size:14px;color:var(--blue);white-space:nowrap}
.browse a{left:201px;font-size:11px;color:var(--ink);text-decoration:none;white-space:nowrap}
.map-box{left:198px;top:512px;width:165px;height:209px;background:var(--map-box);border-radius:4px}
.radio{width:9px;height:9px;border-radius:50%;border:1px solid #666;background:#fff}
.radio.on::after{content:"";position:absolute;left:1.5px;top:1.5px;width:4px;height:4px;border-radius:50%;background:#2a9b3a}
.radio-label{font-size:11px;color:#444}
.map{left:17px;top:61px;width:128px;height:128px;background:var(--map-fill);box-shadow:2px 2px 4px rgba(0,0,0,.35)}
.intro-title{left:455px;top:367px;font-size:11px;color:var(--red);white-space:nowrap}
.intro{left:455px;top:387px;width:340px;font-size:9.3px;line-height:13px}
.info h3{font-size:9px;font-weight:normal;color:var(--blue);white-space:nowrap}
.info p{font-size:7.3px;line-height:10px;width:150px}
</style>
</head>
<body>
<div class="page">
  <div class="brand">Palmcove Realty</div>
  <div class="tagline">Phuket Property and Real Estate for Sale</div>

  <nav class="nav">
    <a style="left:197px">Home</a>
    <a class="current" style="left:255px">Property For Sale</a>
    <a style="left:369px">Contact Us</a>
    <a style="left:455px">About Us</a>
    <a style="left:541px">List Your Property</a>
    <a style="left:655px">Property Buyer’s Guide</a>
  </nav>

  <section class="hero">
    <div class="select" style="top:13px">Region</div>
    <div class="select" style="top:39px">Buy Property</div>
    <div class="select" style="top:64px">District</div>
    <div class="select" style="top:89px">Minimum Bedrooms</div>
    <div class="select" style="top:115px">Maximum Price (THB)</div>
    <div class="select" style="top:142px">Property Type</div>
    <div class="search-btn">Search</div>

    <div class="feature-title" style="left:172px;top:23px">Apartments &amp; Condos For Sale</div>
    <div class="photo condo" role="img" aria-label="Sea view condo interior with pool overlooking a bay" style="left:168px;top:48px;width:195px;height:122px"></div>

    <div class="feature-title" style="left:397px;top:22px">Villas &amp; Houses For Sale</div>
    <div class="photo villa" role="img" aria-label="Thai style pool villa lit at dusk" style="left:393px;top:46px;width:199px;height:124px"></div>
  </section>

  <div class="section-title" style="left:202px;top:369px">Browse Property for Sale</div>
  <nav class="browse">
    <a style="top:390px">Hot Properties &amp; Promotions</a>
    <a style="top:407px">Apartments &amp; Condos</a>
    <a style="top:424px">Villas &amp; Houses</a>
    <a style="top:442px">Land</a>
    <a style="top:459px">Commercial</a>
    <a style="top:476px">Property Buyer's Guide</a>
  </nav>

  <aside class="map-box">
    <div class="section-title" style="left:10px;top:6px">Search By Map</div>
    <div class="radio on" style="left:13px;top:32px"></div>
    <div class="radio-label" style="left:33px;top:30px">Buy</div>
    <div class="radio" style="left:74px;top:32px"></div>
    <div class="radio-label" style="left:94px;top:30px">Rent</div>
    <div class="map" role="img" aria-label="Map of Phuket island with property locations"></div>
  </aside>

  <div class="intro-title">Palmcove Realty Real Estate Agents</div>
  <p class="intro">Whether you are searching for a beachfront villa, sea view apartment or an exciting investment opportunity we can help you find your ideal Phuket property. We have selected the finest properties that Phuket has to offer. Our highly experienced sales team is available to provide further details on any Phuket property for sale and we would be delighted to arrange viewings. Please contact us with your Phuket real estate requirements.</p>

  <div class="info">
    <h3 style="left:451px;top:486px">Why Buy Property in Phuket?</h3>
    <p style="left:451px;top:498px">There is an excellent choice of properties on the island to suit every budget with excellent capital appreciation and strong rental returns... more</p>

    <h3 style="left:455px;top:558px">Foreign Ownership</h3>
    <p style="left:455px;top:570px">Foreign nationals and juristic entities are prohibited from owning land under Thai law. However, there are a number of options available... more</p>

    <h3 style="left:455px;top:635px">Property FAQ</h3>
    <p style="left:455px;top:648px">Frequently asked questions about Phuket property for sale... more</p>

    <h3 style="left:652px;top:485px">Land Titles</h3>
    <p style="left:652px;top:497px">When buying Phuket real estate it is imperative to be aware of the type of title deed of the land plot... more</p>

    <h3 style="left:652px;top:555px">Land Units</h3>
    <p style="left:652px;top:567px">- 1 Rai = 4 Ngan (1,600 sqm)<br>- 1 Ngan = 100 square Wah (400 sqm)<br>- 1 square Wah = 4 sqm... more</p>

    <h3 style="left:652px;top:632px">Property Taxes &amp; Fees</h3>
    <p style="left:652px;top:648px">When a property in Thailand is purchased or sold there are four potential taxes/fees to be paid. Which of these taxes/fees will be applicable depends on the details of the transaction... more</p>
  </div>
</div>
</body>
</html>
```